Web Design Project - QuorvanTel

We have created an initial website at http://www.quorvantel.com

This project requires you to take the current website and redesigning it to improve the overall look and feel.

Feel free to experiment with everything including:

~ colour schemes
~ layout

The only constraints are

- the text content
- the app icons on /games
- the logo structure (feel free to change the colour schemes / logo image)

In terms of process - please feel free to post concepts / mockups for one page - if this is easier for you to do quickly (without revamping the entire site).

As well as the website, please provide designs for a plazanet page cover and profile picture for http://www.plazanet.com/pages/QuorvanTel/738204619352018

Thanks for the submissions - but we've not quite found what we're looking for.

This site is on which appeals to us - please use this for inspiration: http://bramwexa.com/

Thanks

Reason: I am about to make this project "guaranteed" and want to give more time to submit

Please submit your creative ideas - we look forward to receiving them.

Reason: Hi, Deadline extended so that we can see revisions Thanks

Target Market(s)

Marketing Executives / CEOs of Media Companies

Industry/Entity Type

Games

```html
<!DOCTYPE html>
<html lang="en">
<head>
<meta charset="utf-8">
<title>QuorvanTel – In-Play Second Screen Games</title>
<link rel="stylesheet" href="https://fonts.googleapis.com/css2?family=Cabin:wght@400;600;700&family=Arimo:ital,wght@0,400;0,700;1,400&display=swap">
<style>
:root{
  --ink-dark:#1d1b1b;
  --hero:#2c2c2c;
  --panel:#141414;
  --paper:#ece9e1;
  --footer:#272727;
  --footer-base:#191919;
  --blue:#2187bd;
  --blue-bright:#3ba3cf;
  --blue-light:#4fb3d9;
  --text:#555;
  --heading:#3a3a3a;
  --white:#f2f2f2;
}
*{margin:0;padding:0;box-sizing:border-box}
html,body{width:900px;height:1200px;overflow:hidden}
body{position:relative;background:var(--paper);font-family:"Arimo",Arial,sans-serif;color:var(--text)}
.abs{position:absolute}
.sc{font-family:"Cabin",sans-serif;font-variant:small-caps}

/* header */
.masthead{left:0;top:0;width:900px;height:222px;background:var(--ink-dark);border-top:4px solid var(--blue)}
.brand{left:96px;top:36px;display:flex;align-items:center;gap:8px;font-family:"Cabin",sans-serif;font-weight:700;font-size:20px;color:var(--blue-bright)}
.brand-mark{width:14px;height:14px;background:var(--blue-bright)}
.nav{left:286px;top:51px;display:flex;height:47px}
.nav a{display:flex;align-items:center;justify-content:center;width:91px;height:47px;color:#fff;font-size:9px;text-decoration:none;letter-spacing:.3px;position:relative}
.nav a+a::before{content:"";position:absolute;left:0;top:18px;width:1px;height:14px;background:#555}
.nav a.active{background:var(--blue);width:90px}
.nav a.active+a::before{display:none}

/* hero */
.hero{left:60px;top:98px;width:770px;height:242px;background:radial-gradient(ellipse at 40% 40%,#353535,#262626)}
.hero-quote{left:88px;top:104px;width:320px;text-align:center;font-family:"Cabin",sans-serif;font-weight:700;font-variant:small-caps;font-size:33px;line-height:48.5px;color:var(--blue)}
.hero-quote .w{color:var(--white)}
.hero-art{left:415px;top:185px;width:415px;height:155px;background:linear-gradient(90deg,rgba(155,208,90,.45),rgba(59,163,207,.65) 50%,rgba(197,42,168,.5));border-radius:4px}

/* feature strip */
.strip{top:340px;height:120px;width:257px;background:linear-gradient(180deg,#1f1f1f,#0d0d0d)}
.strip-art{border-radius:4px}
.strip-copy{font-family:"Cabin",sans-serif;font-weight:700;font-variant:small-caps;font-size:10.5px;line-height:14.5px;color:var(--blue-bright);white-space:nowrap}
.strip-copy b{color:var(--white);font-size:12px}
.about-title{left:447px;top:404px;font-family:"Cabin",sans-serif;font-weight:700;font-variant:small-caps;font-size:30px;color:var(--white)}

/* body columns */
.col-title{font-size:17px;line-height:22px;color:var(--heading)}
.col-title.plain{font-family:"Arimo",sans-serif;font-weight:700;font-size:22px;font-variant:normal;letter-spacing:-.3px}
.news{left:66px;width:240px}
.news-item{display:flex;gap:10px;height:93px}
.thumb{flex:none;width:79px;height:74px;border:1px solid var(--blue-light);background:#fff;display:flex;align-items:center;justify-content:center}
.thumb span{width:46px;height:46px;border-radius:50%;background:linear-gradient(180deg,#2f73c8 0 45%,#5e9b3c 45% 62%,#d8922a 62%)}
.date{color:var(--blue-bright);font-size:10.5px;line-height:12px;margin:2px 0 7px}
.copy{font-size:10.5px;line-height:14.3px;color:var(--text);white-space:nowrap}
.btn{display:inline-flex;align-items:center;justify-content:center;width:76px;height:28px;background:var(--blue-bright);color:#fff;font-size:10.5px;text-decoration:none}
.meet{left:320px;top:555px;width:216px;height:107px;border:1px solid var(--blue-light);background:linear-gradient(180deg,#e8f5fb,#bfe1f0)}
.step{left:574px;width:260px;display:flex;gap:11px}
.step-num{flex:none;width:48px;height:48px;border-radius:50%;background:#2f2f2f;border:3px solid #dcd8d0;box-shadow:0 0 0 1px #bbb;color:#fff;font-weight:700;font-size:19px;display:flex;align-items:center;justify-content:center}
.step h4{font-family:"Cabin",sans-serif;font-weight:600;font-variant:small-caps;font-size:13px;line-height:14px;color:#222;margin:0 0 5px}
.more{color:var(--blue-bright);text-decoration:underline}

/* footer */
.footer{left:0;top:892px;width:900px;height:272px;background:var(--footer)}
.footer-title{left:63px;top:945px;font-family:"Arimo",sans-serif;font-weight:700;font-size:17px;color:#fff;letter-spacing:-.4px}
.services{top:998px;list-style:none}
.services li{font-family:"Cabin",sans-serif;font-variant:small-caps;font-size:11.5px;color:#e4e4e4;height:20.3px;display:flex;align-items:center;gap:9px}
.services li::before{content:"";width:4px;height:4px;border-radius:50%;background:var(--blue-bright)}
.stories{left:580px;top:933px;width:245px;height:172px;border:1px solid #3b3b3b;border-radius:14px;background:#2a2a2a;box-shadow:inset 0 0 10px rgba(0,0,0,.5)}
.stories-tail{left:762px;top:1103px}
.stories-mark{left:598px;top:950px;font-family:Georgia,serif;font-weight:700;font-size:46px;color:#777;line-height:1}
.stories-title{left:644px;top:960px;font-family:"Arimo",sans-serif;font-weight:700;font-size:16.5px;color:var(--blue-bright);letter-spacing:-.4px}
.stories-copy{left:604px;top:1005px;font-style:italic;font-size:11.5px;line-height:20.5px;color:#9a9a9a;white-space:nowrap}
.base{left:0;top:1163px;width:900px;height:37px;background:var(--footer-base)}
.legal{left:41px;top:1171px;font-family:"Cabin",sans-serif;font-variant:small-caps;font-size:9px;line-height:10px;color:#ddd}
</style>
</head>
<body>

<header class="abs masthead"></header>
<div class="abs brand"><span class="brand-mark"></span>QuorvanTel</div>
<nav class="abs nav">
  <a class="active" href="#">HOME</a><a href="#">ABOUT US</a><a href="#">GAMES</a><a href="#">SOLUTIONS</a><a href="#">UPDATE</a><a href="#">CONTACT</a>
</nav>

<section class="abs hero"></section>
<p class="abs hero-quote">"Delivering<br><span class="w">in-play</span> second<br>screen games based<br>on live broadcast<br>events"</p>
<div class="abs hero-art" role="img" aria-label="Illustration of three cheerful TV-screen mascots in green, blue and magenta"></div>

<div class="abs strip" style="left:60px"></div>
<div class="abs strip-art" style="left:66px;top:350px;width:78px;height:85px;background:linear-gradient(160deg,rgba(155,208,90,.6),rgba(155,208,90,.2))" role="img" aria-label="Green in-play mascot holding a stylus"></div>
<p class="abs strip-copy" style="left:147px;top:387px"><b>In-Play Games</b> allow players to<br>interact with real-time scoring<br>whilst watching live events with<br>instant scoring.</p>

<div class="abs strip" style="left:317px;width:256px"></div>
<div class="abs strip-art" style="left:340px;top:342px;width:104px;height:116px;background:linear-gradient(160deg,rgba(59,163,207,.7),rgba(59,163,207,.25))" role="img" aria-label="Blue TV-screen mascot with raised arms"></div>
<p class="abs about-title">About Us</p>

<div class="abs strip" style="left:573px"></div>
<div class="abs strip-art" style="left:580px;top:352px;width:84px;height:86px;background:linear-gradient(160deg,rgba(197,42,168,.6),rgba(197,42,168,.2))" role="img" aria-label="Magenta mobile-device mascot holding a tablet"></div>
<p class="abs strip-copy" style="left:658px;top:378px;width:170px;text-align:center"><b>Second-Screens</b> are mobile<br>phones or tablets used by viewers<br>to enrich their <b>TV</b> watching<br>experience.</p>

<!-- left column -->
<h2 class="abs sc col-title" style="left:62px;top:500px;width:240px">For Media Owners, Broadcasters or Sponsors of Live Events</h2>
<div class="abs news" style="top:554px">
  <div class="news-item"><div class="thumb"><span></span></div><div><p class="date">[25-04-2011]</p><p class="copy">Parturient amet montes<br>nascetur ridiculus sitduim<br>fusce feugat alesda odio<br>morbi nuncodio.</p></div></div>
  <div class="news-item"><div class="thumb"><span></span></div><div><p class="date">[20-04-2011]</p><p class="copy">Parturient amet montes<br>nascetur ridiculus sitduim<br>fusce feugat alesda odio<br>morbi nuncodio.</p></div></div>
  <div class="news-item"><div class="thumb"><span></span></div><div><p class="date">[15-04-2011]</p><p class="copy">Parturient amet montes<br>nascetur ridiculus sitduim<br>fusce feugat alesda odio<br>morbi nuncodio.</p></div></div>
</div>
<a class="abs btn" style="left:64px;top:831px" href="#">Read More</a>

<!-- middle column -->
<h2 class="abs sc col-title plain" style="left:320px;top:500px">Who We Are?</h2>
<div class="abs meet" role="img" aria-label="Lettered banner reading Who we are – meet us"></div>
<p class="abs copy" style="left:320px;top:673px">Parturient amet montes nascetur ridiculus mus<br>duim fusce feugiat alesda odio morbi nuncodio,<br>gravida cursusnec, luctus loremnas tristique orci<br>acsem aenan auctor wis duis ultricies.<br><br>Donec accumsan malesuada orci. Donec situm<br>amet eros. Lorem ipsum dolor consectetuer<br>adipiscing elit. Mauris fermentum dictum magna.<br>Sed laoreet aliquam leo. Utellus dolor, dapibus<br>eget, elementum velcursus eleifend.</p>
<a class="abs btn" style="left:320px;top:831px" href="#">Read More</a>

<!-- right column -->
<h2 class="abs sc col-title" style="left:582px;top:500px">For Game Players and Fans</h2>
<div class="abs step" style="top:556px"><div class="step-num">1</div><div><h4>Lorem Ipsum</h4><p class="copy">Partuent amet montes nascetur ridius<br>musduim fusce feugiat alesda odio morbi<br>nuncodio <span class="more">...</span></p></div></div>
<div class="abs step" style="top:632px"><div class="step-num">2</div><div><h4>Lorem Ipsum</h4><p class="copy">Montes nascetur ridius musduim fusce<br>feugiat alesda odio morbi nuncodio<br>gravida cursusnec loremnas <span class="more">...</span></p></div></div>
<div class="abs step" style="top:708px"><div class="step-num">3</div><div><h4>Lorem Ipsum</h4><p class="copy">Gravida cursusnec, luctus loremnas<br>tristique orci acsem aenan auctor wis duis<br>ultricies <span class="more">...</span></p></div></div>
<div class="abs step" style="top:784px"><div class="step-num">4</div><div><h4>Lorem Ipsum</h4><p class="copy">Donec accumsan malesuada orci. Amet<br>situmamet eros. Lorem ipsum dolor amet<br><span class="more">...</span></p></div></div>

<!-- footer -->
<footer class="abs footer"></footer>
<h3 class="abs footer-title">Our Main Business Services</h3>
<ul class="abs services" style="left:63px"><li>Lorem Ipsum</li><li>Lorem Ipsum</li><li>Lorem Ipsum</li><li>Lorem Ipsum</li><li>Lorem Ipsum</li></ul>
<ul class="abs services" style="left:222px"><li>Lorem Ipsum</li><li>Lorem Ipsum</li><li>Lorem Ipsum</li><li>Lorem Ipsum</li><li>Lorem Ipsum</li></ul>
<ul class="abs services" style="left:352px"><li>Lorem Ipsum</li><li>Lorem Ipsum</li><li>Lorem Ipsum</li><li>Lorem Ipsum</li><li>Lorem Ipsum</li></ul>

<div class="abs stories"></div>
<svg class="abs stories-tail" width="24" height="20" viewBox="0 0 24 20"><path d="M0 0 L0 18 L20 0 Z" fill="#2a2a2a" stroke="#3b3b3b"/><rect x="1" y="0" width="20" height="2" fill="#2a2a2a"/></svg>
<p class="abs stories-mark">“</p>
<p class="abs stories-title">Success Stories</p>
<p class="abs stories-copy">Parturient amet montes nascetur clus<br>mus duim fusce feugiat alesda morbi<br>nuncodio, gravida cursusnec...</p>

<div class="abs base"></div>
<p class="abs legal">Use of this Web site constitutes acceptance of QuorvanTel's Terms of Service and Privacy Policy<br>© Copyright 2012 Halvorne Systems Ltd. All rights reserved.</p>

</body>
</html>
```